Stationary design for boutique production house

We need a stationary design for our production house, 'Lorin Studios' based in Singapore. We produce microfilms as well as podcasts, talkshows and events. Our logo is a stylized icon of our director, who is also the executive producer and host of our programs, Lorin. Our main company colors are Red, Black and white. We would like a clean, minimalist design incorporating our existing company logo that conveys a sense of urbanism and elegance.

Logo and font files are attached. f

Target Market(s)

We focus on lifestyle media rather than entertainment.

Industry/Entity Type

Boutique

Font styles to use
Serif
Sans Serif

Colors
ec1f27
ffffff
000000

Requirements
Must have
• Our company logo and at least one of our company colors.
Nice to have
• Our address and contact information.
Should not have
• Changes made to the company logo (using only certain parts of it is fine though)

```html
<!DOCTYPE html>
<html lang="en">
<head>
<meta charset="utf-8">
<title>Lorin Studios — Stationery</title>
<link href="https://fonts.googleapis.com/css2?family=Arimo:wght@400;700&display=swap" rel="stylesheet">
<style>
  :root {
    --red: #f50a16;
    --ink: #1e1710;
    --paper: #ffffff;
    --paper-soft: #f8f8f8;
    --stage: #eceef1;
    --muted: #b4b4b4;
  }
  * { margin: 0; padding: 0; box-sizing: border-box; }
  html, body { width: 1200px; height: 1003px; overflow: hidden; }
  body {
    background: var(--stage);
    font-family: "Arimo", Arial, sans-serif;
    position: relative;
  }
  .sheet { position: absolute; }

  /* Letterhead */
  .letterhead {
    left: 45px; top: 18px; width: 547px; height: 775px;
    background: var(--paper);
    border-bottom: 6px solid var(--red);
    z-index: 2;
  }
  .letterhead .mark-box {
    position: absolute; left: 54px; top: 55px; width: 100px; height: 100px;
    background: var(--red);
    display: flex; flex-direction: column; align-items: center; justify-content: center; gap: 10px;
  }
  .wordmark { font-weight: 400; text-align: center; line-height: 1.1; }
  .mark-box .wordmark { color: var(--paper); font-size: 12px; }
  .dot { border-radius: 50%; background: currentColor; display: block; }
  .mark-box .dot { width: 12px; height: 12px; color: var(--paper); }

  .contact-row { position: absolute; top: 729px; left: 64px; display: flex; gap: 20px; }
  .contact { display: flex; align-items: center; gap: 6px; color: var(--muted); font-size: 10px; letter-spacing: 1px; }
  .contact svg { width: 15px; height: 15px; flex: none; }

  /* Second sheet */
  .second-sheet {
    left: 283px; top: 208px; width: 547px; height: 774px;
    background: var(--paper-soft);
    z-index: 1;
  }
  .second-sheet .red-band {
    position: absolute; left: 0; top: 153px; width: 100%; height: 461px; background: var(--red);
  }
  .second-sheet .mark-panel {
    position: absolute; left: 357px; top: 307px; width: 190px; height: 153px;
    background: var(--paper-soft);
    display: flex; flex-direction: column; align-items: center; justify-content: center; gap: 14px;
  }
  .mark-panel .wordmark { color: var(--ink); font-size: 16px; }
  .mark-panel .dot, .card .dot { width: 10px; height: 10px; color: var(--red); }
  .sheet-details { position: absolute; color: var(--muted); font-size: 10px; letter-spacing: 1px; }

  /* Business cards */
  .card {
    width: 267px; height: 152px; background: var(--paper-soft);
    border-top: 3px solid var(--red); border-bottom: 3px solid var(--red);
  }
  .card-front { left: 868px; top: 74px; display: flex; flex-direction: column; align-items: center; justify-content: center; gap: 10px; }
  .card-front .wordmark { color: var(--ink); font-size: 12px; }
  .card-back { left: 872px; top: 264px; width: 268px; }
  .card-back .holder { position: absolute; left: 17px; top: 44px; color: var(--muted); }
  .holder .name { font-size: 14px; font-weight: 700; letter-spacing: 1.2px; }
  .holder .role { font-size: 10px; letter-spacing: 1px; margin-top: 1px; }
  .card-back .card-contacts { position: absolute; left: 126px; top: 44px; display: flex; flex-direction: column; gap: 14px; }
  .card-back .contact { font-size: 7px; gap: 5px; }
  .card-back .contact svg { width: 13px; height: 13px; }
</style>
</head>
<body>
  <svg width="0" height="0" style="position:absolute">
    <defs>
      <symbol id="icon-mail" viewBox="0 0 16 16"><circle cx="8" cy="8" r="8" fill="#f50a16"/><rect x="4" y="5" width="8" height="6" rx="0.6" fill="#fff"/><path d="M4.3 5.4 8 8.3l3.7-2.9" fill="none" stroke="#f50a16" stroke-width="0.9"/></symbol>
      <symbol id="icon-web" viewBox="0 0 16 16"><circle cx="8" cy="8" r="8" fill="#f50a16"/><g fill="none" stroke="#fff" stroke-width="0.9"><circle cx="8" cy="8" r="4.2"/><ellipse cx="8" cy="8" rx="1.8" ry="4.2"/><path d="M3.8 8h8.4M4.4 6h7.2M4.4 10h7.2"/></g></symbol>
      <symbol id="icon-phone" viewBox="0 0 16 16"><circle cx="8" cy="8" r="8" fill="#f50a16"/><path d="M5.2 4.2l1.5-.3 1 2.1-1 .8c.5 1.1 1.3 1.9 2.4 2.4l.8-1 2.1 1-.3 1.5c-3.6.3-6.8-2.9-6.5-6.5z" fill="#fff"/></symbol>
    </defs>
  </svg>

  <section class="sheet second-sheet">
    <div class="red-band"></div>
    <div class="mark-panel">
      <span class="dot"></span>
      <span class="wordmark">Lorin Studios</span>
    </div>
    <p class="sheet-details" style="left:33px;top:640px">hello@lorinmedia.sg</p>
    <p class="sheet-details" style="left:339px;top:640px">address: 18 Amoy St, #02</p>
    <p class="sheet-details" style="left:33px;top:680px">lorinmedia.sg</p>
    <p class="sheet-details" style="left:33px;top:709px">6123 4567</p>
  </section>

  <section class="sheet letterhead">
    <div class="mark-box">
      <span class="dot"></span>
      <span class="wordmark">Lorin Studios</span>
    </div>
    <div class="contact-row">
      <span class="contact"><svg><use href="#icon-mail"/></svg>hello@lorinmedia.sg</span>
      <span class="contact" style="margin-left:22px"><svg><use href="#icon-web"/></svg>lorinmedia.sg</span>
      <span class="contact" style="margin-left:58px"><svg><use href="#icon-phone"/></svg>6123 4567</span>
    </div>
  </section>

  <section class="sheet card card-front">
    <span class="dot"></span>
    <span class="wordmark">Lorin Studios</span>
  </section>

  <section class="sheet card card-back">
    <div class="holder">
      <p class="name">Your Name</p>
      <p class="role">Position</p>
    </div>
    <div class="card-contacts">
      <span class="contact"><svg><use href="#icon-phone"/></svg>6123 4567</span>
      <span class="contact"><svg><use href="#icon-web"/></svg>lorinmedia.sg</span>
      <span class="contact"><svg><use href="#icon-mail"/></svg>hello@lorinmedia.sg</span>
    </div>
  </section>
</body>
</html>
```